Flyer for an anniversary promotion

2nd year anniversary promotion flyer for Harwick Dental (logo attached)
Size A4
Promotion runs from Now until 31st Dec 2024
Leave room for actual promotional text which will be in multiple languages (~50 words)
Brand associations
Modern, classy, high quality service, customer care

NOTE - Company SELLS to dental clinics but Harwick is a dental products company, not dentists/dental clinics/etc.

Pixelmarket wants this to be 300+ words

Target Market(s)

Dental clinics

Industry/Entity Type

Dental

Requirements
Should not have
• Don't use images of teeth

```html
<!DOCTYPE html>
<html lang="en">
<head>
<meta charset="utf-8">
<title>Harwick Dental – 2 Years Anniversary</title>
<link href="https://fonts.googleapis.com/css2?family=Poppins:wght@400;600;700;800&family=Great+Vibes&display=swap" rel="stylesheet">
<style>
  :root{
    --navy:#0b4870;
    --sky:#4a9fd0;
    --mist:#c5dae2;
    --white:#ffffff;
    --ink:#1b1b1b;
    --title-blue:#1f4fa0;
  }
  *{margin:0;padding:0;box-sizing:border-box}
  html,body{width:848px;height:1200px;overflow:hidden;background:var(--white)}
  .flyer{position:relative;width:848px;height:1200px;overflow:hidden;background:var(--mist);font-family:"Poppins",sans-serif;color:var(--ink)}
  .backdrop{position:absolute;inset:0}
  .brand-tab{position:absolute;left:640px;top:0;width:134px;height:194px;background:var(--mist);border-radius:0 0 67px 67px;text-align:center;padding-top:92px}
  .brand-tab .brand-name{font-weight:600;font-size:15px;letter-spacing:1px;color:var(--navy);line-height:1.2}
  .brand-tab .brand-sub{font-weight:600;font-size:9px;letter-spacing:3px;color:var(--navy);line-height:1.3}
  .headline{position:absolute;right:36px;top:305px;text-align:right;color:var(--white)}
  .headline .big{font-weight:700;font-size:57px;line-height:56px;letter-spacing:0.5px}
  .headline .sub{font-weight:600;font-size:24px;line-height:34px;margin-top:6px}
  .badge-num{position:absolute;left:290px;top:478px;width:80px;text-align:center;font-weight:800;font-size:112px;line-height:112px;color:var(--white)}
  .badge-script{position:absolute;left:334px;top:544px;font-family:"Great Vibes",cursive;font-size:28px;color:var(--white);line-height:1}
  .badge-label{position:absolute;left:348px;top:571px;font-size:5px;letter-spacing:1px;color:var(--white);font-weight:600}
  .intro{position:absolute;left:34px;top:634px;width:430px;font-size:14.5px;line-height:22.6px}
  .services-pill{position:absolute;left:525px;top:578px;width:229px;height:54px;border-radius:27px;background:var(--navy);color:var(--white);font-weight:700;font-size:17px;letter-spacing:1.5px;display:flex;align-items:center;justify-content:center}
  .service{position:absolute;left:590px;width:220px}
  .service h3{font-weight:700;font-size:14.5px;line-height:17px;color:var(--title-blue)}
  .service p{font-size:12px;line-height:16.2px;margin-top:3px}
  .service-icon{position:absolute;width:54px;height:54px;border-radius:50%}
  .service-icon.dark{background:var(--navy)}
  .service-icon.light{background:var(--sky)}
  .contact-line{position:absolute;left:69px;display:flex;align-items:center;gap:13px;font-size:17px}
  .contact-line svg{flex:none}
  .call{position:absolute;right:148px;top:1068px;text-align:right;color:var(--white)}
  .call .label{font-weight:700;font-size:20px;line-height:24px}
  .call .number{font-weight:700;font-size:29px;line-height:36px}
</style>
</head>
<body>
<div class="flyer">
  <svg class="backdrop" width="848" height="1200" viewBox="0 0 848 1200" aria-hidden="true">
    <defs>
      <linearGradient id="roomTones" x1="0" y1="0" x2="1" y2="1">
        <stop offset="0" stop-color="#f2f5f7"/>
        <stop offset="0.5" stop-color="#d6e1e8"/>
        <stop offset="1" stop-color="#9fb4c2"/>
      </linearGradient>
    </defs>
    <!-- navy top field with curved edge -->
    <path d="M0 0 H848 V432 C720 500 560 540 430 529 L0 529 Z" fill="var(--navy)"/>
    <!-- sky band under the curve -->
    <path d="M430 529 C560 540 720 500 848 432 V450 C720 520 560 558 430 548 Z" fill="var(--sky)"/>
    <!-- dotted grids -->
    <g fill="var(--white)">
      <circle cx="255" cy="57" r="2.4"/><circle cx="278" cy="57" r="2.4"/><circle cx="302" cy="57" r="2.4"/><circle cx="325" cy="57" r="2.4"/>
      <circle cx="255" cy="76" r="2.4"/><circle cx="278" cy="76" r="2.4"/><circle cx="302" cy="76" r="2.4"/><circle cx="325" cy="76" r="2.4"/>
      <circle cx="255" cy="96" r="2.4"/><circle cx="278" cy="96" r="2.4"/><circle cx="302" cy="96" r="2.4"/><circle cx="325" cy="96" r="2.4"/>
      <circle cx="255" cy="115" r="2.4"/><circle cx="278" cy="115" r="2.4"/><circle cx="302" cy="115" r="2.4"/><circle cx="325" cy="115" r="2.4"/>
    </g>
    <g fill="var(--navy)">
      <circle cx="11" cy="918" r="2.4"/><circle cx="30" cy="918" r="2.4"/>
      <circle cx="11" cy="936" r="2.4"/><circle cx="30" cy="936" r="2.4"/>
      <circle cx="11" cy="953" r="2.4"/><circle cx="30" cy="953" r="2.4"/>
      <circle cx="11" cy="971" r="2.4"/><circle cx="30" cy="971" r="2.4"/>
    </g>
    <!-- photo frame -->
    <circle cx="146" cy="336" r="284" fill="var(--sky)"/>
    <circle cx="146" cy="336" r="271" fill="url(#roomTones)" role="img" aria-label="Photo of a bright modern dental treatment room with chair, instrument tray and control panel"/>
    <!-- anniversary badge -->
    <circle cx="345" cy="537" r="84" fill="var(--sky)"/>
    <circle cx="345" cy="537" r="71" fill="var(--sky)" stroke="var(--white)" stroke-width="1.5" stroke-opacity="0.8"/>
    <!-- bottom band -->
    <rect x="0" y="1150" width="848" height="50" fill="var(--sky)"/>
    <!-- contact block -->
    <path d="M408 1200 C410 1100 470 1045 560 1045 L848 1045 V1200 Z" fill="var(--navy)"/>
    <circle cx="854" cy="1048" r="65" fill="var(--sky)"/>
    <!-- phone button -->
    <circle cx="746" cy="1101" r="31" fill="var(--sky)"/>
    <path d="M736 1089 c2 -2 4 -2 5 0 l3 5 c1 2 0 3 -1 4 l-2 2 c2 4 5 7 9 9 l2 -2 c1 -1 2 -2 4 -1 l5 3 c2 1 2 3 0 5 l-3 3 c-3 2 -8 1 -14 -4 c-6 -5 -10 -11 -10 -16 c0 -2 1 -4 2 -5 z" fill="var(--white)"/>
  </svg>

  <div class="brand-tab">
    <div class="brand-name">HARWICK</div>
    <div class="brand-sub">DENTAL</div>
  </div>

  <div class="headline">
    <div class="big">CELEBRATING</div>
    <div class="big">2 YEARST</div>
    <div class="sub">of Excellence in<br>Dental Products!</div>
  </div>

  <div class="badge-num">2</div>
  <div class="badge-script">Years</div>
  <div class="badge-label">ANNIVERSARY</div>

  <p class="intro">Optimize your oral health with our dental care services. From routine checkups to specialized treatments, we ensure your smile stays healthy and bright. Trust us for expert care and a confident, radiant grin.</p>

  <div class="services-pill">OUR SERVICES</div>

  <div class="service-icon dark" style="left:523px;top:641px"></div>
  <div class="service" style="top:648px">
    <h3>High-Quality Dental<br>Instruments and Tools</h3>
    <p>Supplying advanced dental instruments for procedures and diagnostics, designed for precision and durability.</p>
  </div>

  <div class="service-icon light" style="left:523px;top:754px"></div>
  <div class="service" style="top:769px;left:589px">
    <h3>Dental Hygiene and<br>Infection Control Products</h3>
    <p>Offering a range of products to maintain hygiene standards, including sterilization tools, disinfectants, and protective gear.</p>
  </div>

  <div class="service-icon dark" style="left:521px;top:878px"></div>
  <div class="service" style="top:891px">
    <h3>Innovative Dental<br>Technology and Equipment</h3>
    <p>Providing state-of-the-art dental equipment, from imaging systems to patient care devices, enhancing clinic efficiency and patient experience.</p>
  </div>

  <div class="contact-line" style="top:1041px">
    <svg width="30" height="30" viewBox="0 0 30 30" aria-hidden="true"><circle cx="15" cy="15" r="15" fill="var(--sky)"/><path d="M15 7 a5.5 5.5 0 0 1 5.5 5.5 c0 4 -5.5 10 -5.5 10 s-5.5 -6 -5.5 -10 A5.5 5.5 0 0 1 15 7 z" fill="var(--white)"/><circle cx="15" cy="12.5" r="2" fill="var(--sky)"/></svg>
    <span>48 Linden Row, Maple Town, ST 54321</span>
  </div>
  <div class="contact-line" style="top:1080px">
    <svg width="30" height="30" viewBox="0 0 30 30" aria-hidden="true"><circle cx="15" cy="15" r="15" fill="var(--sky)"/><g fill="none" stroke="var(--white)" stroke-width="1.4"><circle cx="15" cy="15" r="7"/><ellipse cx="15" cy="15" rx="3" ry="7"/><line x1="8" y1="15" x2="22" y2="15"/></g></svg>
    <span>www.harwicksupply.com</span>
  </div>

  <div class="call">
    <div class="label">CONTACT US</div>
    <div class="number">+120-555-0148</div>
  </div>
</div>
</body>
</html>
```